Badass Woman-Owned and Operated Small Law Firm needs Modern & Interesting Powerpoint template...

Mainly need powerpoint template that works with high-quality photos and "clipart", but would also like template for post-card size marketing (invitations or announcements); a banner ad for other websites, a Brindle Hub Banner, and One-Page Newsletter/Flyer template to use as a marketing handout announcing new services, etc. I have a logo and colors and can show some designs we've done on our own to show you what we like.

Target Market(s)

managers of condos and hoas and members of condos and hoas

Industry/Entity Type

Law firm that represents condominiums and HOAs

Requirements
Must have
• use of theme/colors and logo already established
Nice to have
• For the powerpoint, I like faded images in the background along with interesting layout. So tired of just banners at the top and bottom

```html
<!DOCTYPE html>
<html lang="en">
<head>
<meta charset="utf-8">
<title>Cascade Commons Law Group – Presentation Template</title>
<link rel="stylesheet" href="https://fonts.googleapis.com/css2?family=Barlow:wght@500;600&family=Nunito+Sans:wght@600&family=Roboto:wght@400;700&display=swap">
<style>
:root{
  --olive:#959a43;
  --olive-pale:#c9cca2;
  --ink:#2a2a2a;
  --text:#333333;
  --paper:#ffffff;
  --backdrop:#dcdcdc;
}
*{margin:0;padding:0;box-sizing:border-box}
html,body{width:1200px;height:3966px;overflow:hidden}
body{background:linear-gradient(180deg,#e4e4e4,#d6d6d6 50%,#e2e2e2);font-family:"Roboto",sans-serif;color:var(--text);position:relative}
.slide{position:absolute;left:86px;width:1028px;height:578px;background:var(--paper);box-shadow:0 4px 18px rgba(0,0,0,.12);overflow:hidden}
.brand{position:absolute;left:60px;top:22px;display:flex;align-items:center;gap:14px}
.brand-dot{width:46px;height:46px;border-radius:50%;background:var(--olive)}
.brand-name{font-family:"Barlow",sans-serif;font-weight:600;font-size:20px;line-height:21px;color:var(--ink);text-transform:uppercase}
.brand.large{top:29px}
.brand.large .brand-dot{width:60px;height:60px}
.brand.large .brand-name{font-size:24px;line-height:25px}
.tab{position:absolute;left:397px;top:25px;width:631px;height:54px;background:var(--olive);border-radius:27px 0 0 27px;color:#fff;font-family:"Barlow",sans-serif;font-weight:600;font-size:30px;letter-spacing:1px;line-height:54px;padding-left:37px;text-transform:uppercase}
.photo{position:absolute}
.body-text{position:absolute;font-size:17.5px;line-height:35px;text-align:justify;color:var(--text)}

/* cover */
.cover-title{position:absolute;left:57px;top:200px;font-family:"Barlow",sans-serif;font-weight:600;font-size:47px;line-height:57px;color:var(--ink);text-transform:uppercase;letter-spacing:.5px}
.cover-sub{position:absolute;left:57px;top:380px;font-size:16.5px;line-height:27px;color:var(--text)}
.cover-disc{position:absolute;left:527px;top:99px;width:437px;height:437px;border-radius:50%;background:var(--olive);opacity:.85}

/* about */
.about-photo{left:0;top:160px;width:499px;height:357px;background:linear-gradient(135deg,#6b6e72,#c7c3bd 45%,#3b3a3c)}
.about-frame{position:absolute;left:0;top:172px;width:512px;height:357px;border-right:4px solid var(--olive);border-bottom:4px solid var(--olive)}

/* how we work */
.work{background:linear-gradient(180deg,#f7f7f8,#eceef0 55%,#f4f4f5)}
.work-bg{position:absolute;left:270px;top:330px;width:210px;height:240px;border-radius:50%;background:radial-gradient(ellipse,rgba(220,220,220,.7),rgba(240,240,240,0) 70%)}
.pillar{position:absolute;width:300px;text-align:center}
.pillar-ring{width:246px;height:246px;margin:0 auto;border-radius:50%;border:9px solid var(--olive-pale)}
.pillar-label{margin-top:26px;font-family:"Nunito Sans",sans-serif;font-weight:600;font-size:29px;color:var(--ink)}

/* clients */
.aerial{left:552px;top:131px;width:348px;height:377px;border:3px solid var(--olive);background:linear-gradient(160deg,#2d3a2c,#6c7a4e 40%,#2b3340 80%)}
.building{left:713px;top:293px;width:257px;height:247px;background:linear-gradient(180deg,#9fc1e0,#e9ecef 40%,#7b8088)}

/* testimonial */
.quote{position:absolute;left:74px;top:180px;width:879px;height:330px;background:var(--olive);color:#fff;text-align:center;padding:44px 38px 0;font-size:17px;line-height:35px}
.quote p{text-align:justify;text-align-last:center}
.quote .who{font-weight:700;margin-top:4px}

/* thank you */
.portrait{position:absolute;left:63px;top:134px;width:410px;height:410px;border-radius:50%;border:4px solid var(--olive);background:linear-gradient(180deg,#d7d9d9,#b9bcbc 60%,#3a3a3a)}
.contact-name{position:absolute;left:537px;top:150px;font-family:"Barlow",sans-serif;font-weight:500;font-size:37px;color:var(--ink);text-transform:uppercase}
.contact-role{position:absolute;left:537px;top:202px;font-family:"Barlow",sans-serif;font-weight:600;font-size:37px;color:var(--olive)}
.contact-row{position:absolute;left:537px;display:flex;align-items:center;gap:20px;font-family:"Barlow",sans-serif;font-weight:600;font-size:29px;color:var(--ink)}
.contact-icon{width:71px;height:71px;border-radius:50%;background:var(--olive);display:flex;align-items:center;justify-content:center}
</style>
</head>
<body>

<section class="slide cover" style="top:86px">
  <div class="brand large"><span class="brand-dot"></span><span class="brand-name">Cascade Commons<br>Law Group</span></div>
  <h1 class="cover-title">Cascade Commons<br>Law Group</h1>
  <p class="cover-sub">Serving Washington and Oregon community associations<br>of all ages, shapes, and sizes.</p>
  <div class="cover-disc"></div>
</section>

<section class="slide about" style="top:730px">
  <div class="brand"><span class="brand-dot"></span><span class="brand-name">Cascade Commons<br>Law Group</span></div>
  <h2 class="tab">About Us</h2>
  <div class="about-frame"></div>
  <div class="photo about-photo" role="img" aria-label="Three colleagues reviewing documents together at a table"></div>
  <p class="body-text" style="left:554px;top:178px;width:423px">New firm, same great service! In 2023, we made a cooperative business decision to separate from Harlow Pruitt to create the “Cascade Commons Law Group” to focus on general counsel advice and services for condominium and HOA communities. So, if you’re looking for the same “focused, responsive, and proven” general counsel representation we provided there, you’ve come to the right place!</p>
</section>

<section class="slide work" style="top:1374px">
  <div class="work-bg" role="img" aria-label="Faded stack of smooth stones in the background"></div>
  <div class="brand"><span class="brand-dot"></span><span class="brand-name">Cascade Commons<br>Law Group</span></div>
  <h2 class="tab">How We Work</h2>
  <div class="pillar" style="left:35px;top:171px">
    <div class="pillar-ring" role="img" aria-label="Person using a phone and laptop at a desk" style="background:linear-gradient(135deg,#4b4038,#a89888 55%,#e8e4e0)"></div>
    <div class="pillar-label">Responsive</div>
  </div>
  <div class="pillar" style="left:363px;top:171px">
    <div class="pillar-ring" role="img" aria-label="Hands reviewing papers with a pen and coffee cup" style="background:linear-gradient(135deg,#1f1f22,#d8d4cc 50%,#8a7866)"></div>
    <div class="pillar-label">Ready</div>
  </div>
  <div class="pillar" style="left:691px;top:171px">
    <div class="pillar-ring" role="img" aria-label="Open notebook beside a mug and a plant" style="background:linear-gradient(135deg,#d9c9b5,#f0ece6 45%,#3c4a38)"></div>
    <div class="pillar-label">Efficient</div>
  </div>
</section>

<section class="slide clients" style="top:2017px">
  <div class="brand"><span class="brand-dot"></span><span class="brand-name">Cascade Commons<br>Law Group</span></div>
  <h2 class="tab">Our Clients</h2>
  <p class="body-text" style="left:63px;top:144px;width:444px">Like people, community associations come in all shapes and sizes. From 100-acre HOAs developed in multiple phases over a span of years, to metropolitan mixed-use condominium towers, to five-unit condo historical building condo conversions, to rural road maintenance associations whose documents aren’t at all clear on what laws apply, these communities are our clients. And while communities can be extremely varied in terms of how they look, what their documents say, and the people that inhabit them, as Vera Lindqvist</p>
  <div class="photo aerial" role="img" aria-label="Aerial view of a tree-lined residential neighborhood"></div>
  <div class="photo building" role="img" aria-label="Modern white condominium building"></div>
</section>

<section class="slide testimonial" style="top:2660px">
  <div class="brand"><span class="brand-dot"></span><span class="brand-name">Cascade Commons<br>Law Group</span></div>
  <h2 class="tab">Our Testimonial</h2>
  <blockquote class="quote">
    <p>The group at CCLG shepherded our association through a substantial reorganization of our governance structure and documents. Over the past four years they have shown the ability to think creatively and critically and have made our organization viable for the foreseeable future. Their work has always been professional, timely and delivered as promised. I would recommend them, without reservation, as counsel for any community association or nonprofit.</p>
    <div class="who">-Dale Ferrin</div>
    <div>Community Manager, Summit Ridge Community Management</div>
  </blockquote>
</section>

<section class="slide thanks" style="top:3303px">
  <div class="brand"><span class="brand-dot"></span><span class="brand-name">Cascade Commons<br>Law Group</span></div>
  <h2 class="tab">Thank You</h2>
  <div class="portrait" role="img" aria-label="Portrait of the managing partner"></div>
  <div class="contact-name">Renata Colby</div>
  <div class="contact-role">Managing Partner</div>
  <div class="contact-row" style="top:258px">
    <span class="contact-icon"><svg width="34" height="34" viewBox="0 0 24 24" fill="#fff"><path d="M6.6 10.8a15.1 15.1 0 0 0 6.6 6.6l2.2-2.2c.3-.3.7-.4 1-.2 1.1.4 2.3.6 3.6.6.6 0 1 .4 1 1V20c0 .6-.4 1-1 1A17 17 0 0 1 3 4c0-.6.4-1 1-1h3.5c.6 0 1 .4 1 1 0 1.3.2 2.5.6 3.6.1.3 0 .7-.2 1z"/></svg></span>
    <span>206.555.0142</span>
  </div>
  <div class="contact-row" style="top:355px">
    <span class="contact-icon"><svg width="36" height="36" viewBox="0 0 24 24" fill="none" stroke="#fff" stroke-width="1.8"><rect x="3" y="6" width="18" height="13" rx="1.5"/><path d="M3 7l9 7 9-7"/></svg></span>
    <span>rcolby@cclgnw.com</span>
  </div>
  <div class="contact-row" style="top:452px">
    <span class="contact-icon"><svg width="38" height="38" viewBox="0 0 24 24" fill="none" stroke="#fff" stroke-width="1.6"><circle cx="12" cy="12" r="9"/><ellipse cx="12" cy="12" rx="4" ry="9"/><path d="M3 12h18M4.5 7.5h15M4.5 16.5h15"/></svg></span>
    <span>www.cclgnw.com</span>
  </div>
</section>

</body>
</html>
```